We need a full corporate logo and stationary design for our business oxForge. OxForge provides 3D Printing Services to the Australian Market.

Our predominant market is the Mining and Architectural industries and our secondary market is the Entrepreneur / Start-up sector.

What we are after:

1. Logo
2. Business Card Design
3. Letterhead Design
4. Email Signature Design

File Formats we require in colour, greyscale and Black and White:

1 .AI
2 .EPS
3 .TIF
4 .PDF
5 .PNG (300 dpi)
6 .JPG (300 dpi)
7 .GIF (300 dpi)

• Should Not Have:
- "Clip-Art" should not be used.

```html
<!DOCTYPE html>
<html lang="en">
<head>
<meta charset="utf-8">
<title>OxForge Stationery</title>
<link rel="stylesheet" href="https://fonts.googleapis.com/css2?family=Arimo:wght@400;700&display=swap">
<style>
  :root {
    --backdrop: #eeeeee;
    --paper: #ffffff;
    --ink: #3c3c3c;
    --ink-soft: #7a7a7a;
    --brand-grey: #8a8a8a;
    --cyan: #bfe6f0;
    --yellow: #f7f0b8;
    --magenta: #f5bcd9;
    --green: #dcf5d0;
    --grey-tint: #d2d2d2;
    --shadow: rgba(0, 0, 0, 0.18);
  }
  * { box-sizing: border-box; margin: 0; padding: 0; }
  html, body {
    width: 848px;
    height: 1200px;
    overflow: hidden;
    background: var(--backdrop);
    font-family: "Arimo", Arial, sans-serif;
    color: var(--ink);
  }
  .canvas { position: relative; width: 848px; height: 1200px; }

  .sheet {
    position: absolute;
    background: var(--paper);
    box-shadow: 0 6px 22px var(--shadow);
    overflow: hidden;
  }

  /* Business card */
  .business-card { left: 164px; top: 40px; width: 520px; height: 300px; }
  /* Letterhead */
  .letterhead { left: 144px; top: 380px; width: 560px; height: 792px; }

  .wordmark {
    position: absolute;
    display: flex;
    align-items: center;
    gap: 8px;
    font-weight: 700;
    color: var(--brand-grey);
    letter-spacing: 0.5px;
  }
  .wordmark .mark-square {
    background: var(--brand-grey);
    border-radius: 3px;
  }
  .business-card .wordmark { left: 56px; top: 30px; font-size: 28px; }
  .business-card .wordmark .mark-square { width: 18px; height: 18px; }
  .letterhead .wordmark { left: 34px; top: 40px; font-size: 24px; }
  .letterhead .wordmark .mark-square { width: 15px; height: 15px; }

  .card-web {
    position: absolute;
    left: 56px;
    top: 70px;
    font-size: 10px;
    color: var(--ink);
  }

  .colour-field {
    position: absolute;
    border-radius: 14px;
    background: linear-gradient(90deg,
      var(--cyan) 0%, var(--yellow) 32%, var(--magenta) 62%, var(--grey-tint) 100%);
    opacity: 0.75;
  }
  .business-card .colour-field { left: 150px; top: 150px; width: 352px; height: 120px; }
  .letterhead .colour-field { left: 150px; top: 612px; width: 388px; height: 110px; }

  .company {
    position: absolute;
    font-size: 12px;
    letter-spacing: 1px;
    color: var(--ink-soft);
  }
  .address {
    position: absolute;
    font-size: 6px;
    line-height: 8px;
    text-transform: uppercase;
    color: var(--ink-soft);
  }
  .email { position: absolute; font-size: 6px; color: var(--ink-soft); }

  .business-card .company { left: 40px; top: 186px; }
  .business-card .address { left: 40px; top: 204px; }
  .business-card .email { left: 40px; top: 236px; }

  .letterhead .web-banner {
    position: absolute;
    right: 38px;
    top: 676px;
    font-size: 27px;
    color: var(--ink);
  }
  .letterhead .company { left: 34px; top: 732px; }
  .letterhead .address { left: 34px; top: 748px; }
  .letterhead .contact-line {
    position: absolute;
    left: 150px;
    top: 772px;
    display: flex;
    gap: 14px;
    font-size: 5.5px;
    text-transform: uppercase;
    color: var(--ink-soft);
  }
  .letterhead .email { left: 34px; top: 774px; }
</style>
</head>
<body>
<main class="canvas">

  <section class="sheet business-card" aria-label="Business card">
    <div class="wordmark"><span class="mark-square"></span>oxForge</div>
    <p class="card-web">www.oxforge.com.au</p>
    <div class="colour-field"></div>
    <p class="company">OxForge Australia</p>
    <p class="address">12 Anvil Street<br>Perth WA<br>6000</p>
    <p class="email">hello@oxforge.com.au</p>
  </section>

  <section class="sheet letterhead" aria-label="Letterhead">
    <div class="wordmark"><span class="mark-square"></span>oxForge</div>
    <div class="colour-field"></div>
    <p class="web-banner">www.oxforge.com.au</p>
    <p class="company">OxForge Australia</p>
    <p class="address">12 Anvil Street<br>Perth WA<br>6000</p>
    <p class="email">hello@oxforge.com.au</p>
    <p class="contact-line">
      <span>Phone 08 5550 1234</span>
      <span>Mobile Phone 0400 555 678</span>
      <span>Fax 08 5550 1299</span>
    </p>
  </section>

</main>
</body>
</html>
```